Need 2 sided card for Loomfield Goods Co. Logo supplied.

I am looking for a business card for my online craft supply business.

I have a very simple design already which I am kind of happy with (see attached pdf) - but would like suggestions for something a little more creative. Design MUST be clean. Super clean! Think thin lines and not blocks of color...

Design must be clean and crisp. No other colors other than in palette (see link below)

I would also like to possible incorporate my tagline - maybe on the front but definitely on the back:
"HollowReed Ideas & Hobby Materials"

Logo file is supplied, but I think spacing on the card may required the wording to be moved underneaths the camera icon - which is fine. Font in logo is Maven Pro. OPEN TO USE OF OTHER FONTS ON CARD BUT MUST BE CLEAN DESIGN.

FRONT OF CARD
All information on attached pdf is correct and should be shown in your design.

BACK OF CARD
Needs to show www.tindalerow.example and maybe logo repeat and tagline.

SIZE
New Zealand sized - meaning finished card will be 90 x 55mm
Printing requirements: printed area is 90mm x 55mm with a 2mm bleed all round.

COLORS
Color palette used in logo can be seen here for HEX and RGB reference: http://www.huebankly.example/palette/8627410/website

NOTE: PAYMENT WILL BE MADE FOR THE BEST DESIGN - EVEN IF I DECIDE NOT TO USE IT.
Updates

Thank you all so much for your designs. I will be providing feedback to ALL designers tomorrow. This weekend is a holiday weekend here in New Zealand and so no work for a few days. Thank-you again - I appreciate your time and creativity!

Industry/Entity Type

Camera

Font styles to use
Other font styles liked:
• Maven Pro - open to others

Requirements
Must have
• Clean design. Logo must be prominent for brand recognition. All contact information must be shown.
Nice to have
• Tagline - at least on reverse

```html
<!DOCTYPE html>
<html lang="en">
<head>
<meta charset="utf-8">
<title>Loomfield Goods Co. — Business Card</title>
<link rel="stylesheet" href="https://fonts.googleapis.com/css2?family=Maven+Pro:wght@400;500;700&display=swap">
<style>
  :root {
    --backdrop: #e9e6e1;
    --card: #ffffff;
    --ink: #57585a;
    --orange: #f0643f;
    --olive: #c9c32a;
    --teal: #3aa39b;
    --slate: #6b6c6e;
  }
  * { box-sizing: border-box; margin: 0; padding: 0; }
  html, body {
    width: 1200px; height: 418px; overflow: hidden;
    background: var(--backdrop);
    font-family: "Maven Pro", sans-serif;
    color: var(--ink);
  }
  .stage { position: relative; width: 1200px; height: 418px; }
  .card {
    position: absolute; background: var(--card);
    box-shadow: 0 2px 6px rgba(0,0,0,0.12);
  }
  .card--front { left: 120px; top: 68px; width: 463px; height: 287px; }
  .card--back  { left: 617px; top: 68px; width: 473px; height: 289px; }

  .brand { position: absolute; text-align: center; }
  .brand__mark {
    display: block; margin: 0 auto;
    border-radius: 50%; border: 2px solid var(--ink);
  }
  .brand__name {
    display: block; font-weight: 400; color: var(--ink);
    white-space: nowrap; line-height: 1;
  }
  .card--front .brand { left: 14px; top: 34px; width: 240px; }
  .card--front .brand__mark { width: 58px; height: 58px; }
  .card--front .brand__name { font-size: 27px; margin-top: 18px; }

  .card--back .brand { left: 0; top: 50px; width: 100%; }
  .card--back .brand__mark { width: 60px; height: 60px; }
  .card--back .brand__name { font-size: 34px; margin-top: 20px; }

  .tagline-front {
    position: absolute; right: 18px; top: 60px;
    text-align: right; color: var(--orange);
    font-size: 17px; font-weight: 500; line-height: 23px;
  }

  .name-tab {
    position: absolute; left: 0; top: 206px;
    width: 205px; height: 40px;
    border: 1.5px solid var(--orange); border-left: none;
    border-radius: 0 12px 12px 0;
    color: var(--orange);
    font-size: 19px; font-weight: 700; letter-spacing: 0.5px;
    line-height: 37px; padding-left: 24px;
  }

  .contact-list {
    position: absolute; right: 14px; top: 136px;
    list-style: none; text-align: right;
    font-size: 12px; line-height: 15.6px; color: var(--ink);
  }
  .contact-list li { display: flex; align-items: center; justify-content: flex-end; gap: 6px; }
  .contact-list svg { width: 12px; height: 12px; flex: none; }

  .web-back {
    position: absolute; left: 0; top: 208px; width: 100%;
    text-align: center; font-size: 15px; color: var(--teal);
    letter-spacing: 0.3px;
  }
  .tagline-band {
    position: absolute; left: 19px; top: 244px;
    width: 435px; height: 29px; border-radius: 10px;
    border: 1.5px solid var(--olive); color: var(--ink);
    font-size: 17px; line-height: 26px; text-align: center;
  }
</style>
</head>
<body>
<main class="stage">

  <section class="card card--front" aria-label="Card front">
    <div class="brand">
      <span class="brand__mark"></span>
      <span class="brand__name">Loomfield Goods Co.</span>
    </div>

    <p class="tagline-front">HollowReed Ideas<br>&amp; Hobby Materials</p>

    <div class="name-tab">Mara Tennick</div>

    <ul class="contact-list">
      <li>+64 (0) 3 555 0142
        <svg viewBox="0 0 12 12"><circle cx="6" cy="6" r="6" fill="var(--orange)"/><path d="M4 3.2l1 1.4-.6.7c.4.8 1 1.4 1.8 1.8l.7-.6 1.4 1-.6 1.2C5.6 8.5 3.5 6.4 3.3 4z" fill="#fff"/></svg></li>
      <li>+64 (0) 21 555 01987
        <svg viewBox="0 0 12 12"><circle cx="6" cy="6" r="6" fill="var(--olive)"/><rect x="4.3" y="2.8" width="3.4" height="6.4" rx=".6" fill="#fff"/></svg></li>
      <li>mara.tennick@loomfield.example
        <svg viewBox="0 0 12 12"><circle cx="6" cy="6" r="6" fill="var(--teal)"/><rect x="3" y="4" width="6" height="4" fill="#fff"/><path d="M3 4l3 2.2L9 4" stroke="var(--teal)" stroke-width=".7" fill="none"/></svg></li>
      <li>social.example/loomfield
        <svg viewBox="0 0 12 12"><circle cx="6" cy="6" r="6" fill="var(--slate)"/></svg></li>
      <li>www.tindalerow.example
        <svg viewBox="0 0 12 12"><circle cx="6" cy="6" r="6" fill="var(--teal)"/><path d="M3.5 5h5l-.6 3.2H4.1z" fill="#fff"/></svg></li>
      <li>www.loomfieldnz.example
        <svg viewBox="0 0 12 12"><circle cx="6" cy="6" r="6" fill="var(--orange)"/></svg></li>
    </ul>
  </section>

  <section class="card card--back" aria-label="Card back">
    <div class="brand">
      <span class="brand__mark"></span>
      <span class="brand__name">Loomfield Goods Co.</span>
    </div>
    <p class="web-back">www.tindalerow.example</p>
    <p class="tagline-band">HollowReed Ideas &amp; Hobby Materials</p>
  </section>

</main>
</body>
</html>
```